New Website for IT Services Business

We need an uncoded web design for a new company based in Australia called "Falcon Tech". We offer specialised point of sale (POS) support to the hospitality industry. We already support hundreds of cafes and restaurants. We are also about to launch and promote a range of new services with the offering of General IT Support being the most important. Other additional services to be offered are Falcon Cloud Backup, reselling and supporting Korvel Antivirus and Tresby Apps.

We have a logo design and our colour scheme is based on the logo with the addition of charcoal grey (see attached logos). We want the pages to reflect precision and efficiency with sharp characteristics. It must be professional but playful/fun elements are encouraged.

Our target audience is restaurant and cafe owners who are interested in finding high quality POS and IT support for their business.

The main call to action on the home page should be either 'Let's Meet For Coffee!' or 'Find out more (by completing a form)'. If you are unsure about what the general text should say then you can use 'Lorem Ipsum' where required.

The site must be viewable at different resolutions and on smart phones and tablets.

The website structure will be quite simple. We require:
- one impressive landing page. Visitors will quickly determine our services and that we provide a very high level of service while also offering value for money. Obviously a clear list of links (however/wherever you like) to the other pages.
- Simple pages with a similar layout for the following:
- Services - "POS & IT Support for the Hospitality Industry" being the main one. With complementary services also listed. Another call to action on this page with the option of 'Let's Meet For Coffee' or a "More information/Pricing" form to be completed by the visitor.
- Products - will be a small online storefront for a few simple products.
- About - Business background. 2x Directors with a photo and brief Bio.
- Downloads - A list of free files to download. Includes remote access client software.
- Contact Us - Mailing address, Email addresses and Support phone number.

Please feel free to ask any questions about the design. I will assist as much as possible.

Thank you for viewing. We promise to give constructive feedback to every person who submits a design. Thank you so much.

Target Market(s)

Restaurant and Cafe owners.

Industry/Entity Type

Hospitality

Requirements
Must have
• - Viewable on different resolutions and on smart phones and tablets.
- Clear call to action of EITHER 'Let's Meet For Coffee' or a "More information/Pricing" form to be completed by the visitor.

```html
<!DOCTYPE html>
<html lang="en">
<head>
<meta charset="utf-8">
<title>Falcon Tech – POS &amp; IT Support</title>
<link rel="stylesheet" href="https://fonts.googleapis.com/css2?family=Oswald:wght@400;500&family=Montserrat:ital,wght@0,300;0,400;0,600;0,700&family=Lora:ital,wght@0,400;1,400&display=swap">
<style>
  :root {
    --red: #d71f2b;
    --red-dark: #a90f1b;
    --charcoal: #333333;
    --charcoal-mid: #3b3b3b;
    --band: #555555;
    --ink: #2a2a2a;
    --text: #4a4a4a;
    --muted: #8c8c8c;
    --rule: #e2e2e2;
    --panel: #f4f4f4;
    --white: #ffffff;
  }
  * { box-sizing: border-box; margin: 0; padding: 0; }
  html, body { width: 788px; height: 1200px; overflow: hidden; }
  body {
    position: relative;
    background: var(--white);
    font-family: "Montserrat", Arial, sans-serif;
    color: var(--text);
  }
  .abs { position: absolute; }

  .stage { left: 0; top: 0; width: 788px; height: 390px; background: var(--charcoal); }

  .header {
    left: 92px; top: 12px; width: 603px; height: 80px;
    background: var(--white);
    border-radius: 26px 42px 0 0;
  }
  .brand { left: 12px; top: 16px; display: flex; align-items: center; gap: 10px; }
  .brand-dot { width: 42px; height: 42px; border-radius: 50%; background: var(--red); }
  .brand-name { font-family: "Oswald", sans-serif; font-weight: 500; font-size: 30px; color: var(--ink); letter-spacing: -0.5px; }
  .callout { right: 24px; top: 22px; text-align: right; }
  .callout-line { font-family: "Oswald", sans-serif; font-weight: 500; font-size: 15px; color: var(--ink); }
  .callout-line strong { font-size: 23px; color: var(--red); font-weight: 500; margin-left: 6px; letter-spacing: 0.5px; }
  .callout-mail { font-size: 7.5px; color: var(--ink); margin-top: -2px; }
  .callout-mail span { color: #1a8ad6; }

  .nav {
    left: 92px; top: 92px; width: 603px; height: 42px;
    background: linear-gradient(#dc2331, var(--red-dark));
    border-radius: 0 30px 0 0;
  }
  .nav-links { list-style: none; display: flex; height: 42px; align-items: center; padding-left: 4px; }
  .nav-links li {
    font-family: "Oswald", sans-serif; font-size: 14.5px; color: var(--white);
    padding: 0 9px; line-height: 24px; border-left: 1px solid rgba(255,255,255,0.25);
  }
  .nav-links li:first-child { border-left: none; }
  .social { display: flex; gap: 6px; }
  .nav .social { position: absolute; left: 484px; top: 9px; }
  .social-dot { width: 24px; height: 24px; border-radius: 50%; background: var(--red); border: 2px solid rgba(255,255,255,0.85); }

  .hero { left: 92px; top: 134px; width: 603px; height: 244px; overflow: hidden; }
  .hero-photo {
    position: absolute; inset: 0;
    background: linear-gradient(90deg, #c9d3dc 0%, #dfe7ee 30%, #eef3f8 55%, #f7fafc 100%);
  }
  .hero-copy { left: 250px; top: 66px; width: 340px; }
  .hero-kicker { font-weight: 300; font-size: 19px; color: var(--ink); letter-spacing: 0.3px; line-height: 22px; }
  .hero-title { font-family: "Oswald", sans-serif; font-weight: 500; font-size: 28px; color: var(--red); line-height: 30px; letter-spacing: 0.9px; white-space: nowrap; }
  .hero-text { font-size: 11.3px; color: var(--ink); line-height: 15.5px; margin-top: 4px; }
  .read-more { display: flex; align-items: center; gap: 5px; margin-top: 8px; font-size: 9.5px; color: var(--red); }
  .read-more svg { display: block; }
  .slider-dots { right: 12px; bottom: 12px; display: flex; gap: 3px; }
  .slider-dots span { width: 8px; height: 8px; background: #a9b4bd; }
  .slider-dots span:first-child { background: var(--red); }

  .welcome { left: 93px; top: 404px; width: 196px; }
  .welcome-light { font-weight: 300; font-size: 21px; color: #888; line-height: 24px; }
  .welcome-bold { font-weight: 700; font-size: 21px; color: var(--ink); line-height: 24px; }
  .body-text { font-size: 8.4px; line-height: 13px; color: var(--text); }
  .welcome .body-text { margin-top: 12px; font-size: 8.2px; letter-spacing: -0.1px; }

  .section-title { font-weight: 300; font-size: 16px; color: var(--ink); }
  .section-title em { font-style: normal; color: var(--red); }

  .services { left: 322px; top: 407px; width: 173px; }
  .service-list { list-style: none; margin-top: 6px; }
  .service-list li { font-size: 8.6px; color: var(--muted); line-height: 12px; padding: 4px 0 5px 1px; border-bottom: 1px solid var(--rule); }
  .service-list li:last-child { border-bottom: none; }
  .who { left: 322px; top: 522px; width: 175px; }
  .who .body-text { margin-top: 10px; font-size: 8.2px; letter-spacing: -0.1px; }

  .coffee { left: 521px; top: 409px; width: 174px; height: 221px; background: var(--charcoal-mid); padding: 15px 12px 0; }
  .coffee-title { font-size: 13px; color: var(--white); font-weight: 400; margin-bottom: 8px; }
  .coffee-title strong { font-weight: 700; }
  .field { height: 20px; background: #2b2b2b; border: 1px solid #525252; font-size: 8px; color: #999; padding: 4px 4px; margin-bottom: 6px; }
  .field-row { display: flex; gap: 7px; }
  .field-row .field { flex: 1; }
  .field-area { height: 63px; }
  .submit { width: 53px; height: 19px; background: var(--red); color: var(--white); font-size: 8px; font-weight: 700; text-align: center; line-height: 19px; margin-top: 1px; }

  .support { left: 92px; top: 663px; width: 206px; }
  .support-photo { width: 206px; height: 77px; margin-top: 9px; background: linear-gradient(90deg, #8a99a8, #c8d2db 55%, #eef1f4); }
  .support .body-text { margin-top: 9px; font-size: 8.2px; letter-spacing: -0.1px; }
  .help-btn { display: inline-block; margin-top: 6px; margin-left: -1px; background: var(--red); color: var(--white); font-size: 14px; padding: 0 8px; line-height: 20px; }

  .testimonial { left: 322px; top: 668px; width: 373px; height: 175px; background: var(--panel); border-radius: 4px; padding: 14px 0 0 12px; }
  .testimonial-head { display: flex; align-items: center; gap: 8px; }
  .testimonial-quote { font-size: 8.6px; font-style: italic; font-family: "Lora", Georgia, serif; color: #555; line-height: 14px; width: 312px; margin: 12px 0 0 33px; }
  .testimonial-name { font-family: "Lora", Georgia, serif; font-style: italic; font-size: 9px; color: var(--ink); margin: 3px 0 0 31px; }

  .partners { left: 92px; top: 880px; width: 603px; height: 68px; background: #f2f2f2; border: 1px solid #dcdcdc; border-radius: 4px; }
  .partners-pill { left: 247px; top: -8px; width: 109px; height: 22px; border-radius: 11px; background: #444; color: var(--white); font-size: 11.5px; text-align: center; line-height: 22px; }
  .partner-row { position: absolute; left: 14px; right: 14px; top: 28px; display: flex; justify-content: space-between; align-items: center; }
  .partner { background: #a9a9a9; border-radius: 3px; height: 20px; }

  .band { left: 0; top: 957px; width: 788px; height: 57px; background: var(--band); }
  .band-text { left: 95px; top: 7px; font-family: "Lora", Georgia, serif; font-size: 16.5px; color: var(--white); line-height: 22px; }
  .band .social { position: absolute; left: 611px; top: 18px; }
  .band .social-dot { border: none; }

  .footer { left: 0; top: 1014px; width: 788px; height: 186px; background: var(--charcoal); }
  .foot-col { top: 14px; }
  .foot-head { font-size: 10px; font-weight: 700; color: var(--white); letter-spacing: 0.3px; margin-bottom: 8px; }
  .foot-list { list-style: none; }
  .foot-list li { font-size: 7.5px; color: #bdbdbd; line-height: 19.5px; }
  .foot-text { font-size: 7.5px; color: #bdbdbd; line-height: 12.5px; }
  .foot-time { font-size: 7.5px; color: #777; margin-top: 3px; }
  .foot-rule { left: 92px; top: 116px; width: 603px; height: 1px; background: #444; }
  .foot-mark { left: 378px; top: 100px; width: 32px; height: 32px; border-radius: 50%; background: var(--red); }
  .foot-links { top: 141px; left: 0; width: 788px; display: flex; justify-content: center; gap: 14px; list-style: none; }
  .foot-links li { font-size: 7.5px; color: #bdbdbd; }
  .copyright { top: 162px; left: 0; width: 788px; text-align: center; font-size: 7px; color: #bdbdbd; }
</style>
</head>
<body>

<div class="abs stage"></div>

<header class="abs header">
  <div class="abs brand">
    <span class="brand-dot"></span>
    <span class="brand-name">Falcon Tech</span>
  </div>
  <div class="abs callout">
    <div class="callout-line">CALL US NOW ON: <strong>1300 62 19 40</strong></div>
    <div class="callout-mail">or email us at <span>support@falcontech.com.au</span></div>
  </div>
</header>

<nav class="abs nav">
  <ul class="nav-links">
    <li>HOME</li><li>SERVICES</li><li>PRODUCTS</li><li>ABOUT</li><li>DOWNLOADS</li><li>CONTACT US</li>
  </ul>
  <div class="social" aria-label="Social links">
    <span class="social-dot"></span><span class="social-dot"></span><span class="social-dot"></span>
  </div>
</nav>

<section class="abs hero">
  <div class="hero-photo" role="img" aria-label="Photo of smiling support staff wearing headsets in a bright office"></div>
  <div class="abs hero-copy">
    <div class="hero-kicker">POS &amp; IT SUPPORT FOR</div>
    <div class="hero-title">THE HOSPITALITY INDUSTRY</div>
    <p class="hero-text">Lorem ipsum dolor sit amet, consectetur adipisicing elit, sed do eiusmod tempor incididunt ut labore et dolore magna aliqua.</p>
    <div class="read-more">
      <svg width="10" height="10" viewBox="0 0 10 10"><rect width="10" height="10" fill="#d71f2b"/><path d="M2 5h5M5 3l2 2-2 2" stroke="#fff" stroke-width="1.2" fill="none"/></svg>
      Read more
    </div>
  </div>
  <div class="abs slider-dots"><span></span><span></span><span></span></div>
</section>

<section class="abs welcome">
  <div class="welcome-light">Welcome to</div>
  <div class="welcome-bold">Falcon Tech</div>
  <p class="body-text">Lorem ipsum dolor sit amet, consectetur adipisicing elit, sed do eiusmod tempor incididunt ut labore et dolore magna aliqua. Ut enim ad minim veniam, quis nostrud exercitation ullamco laboris nisi ut aliquip ex ea commodo consequat. Duis aute irure dolor in reprehenderit in voluptate velit esse cillum dolore eu fugiat nulla pariatur. Excepteur sint occaecat cupidatat non proident, sunt in culpa qui officia deserunt mollit anim id est laborum Duis aute irure dolor in reprehenderit in voluptate velit esse cillum dolore eu fugiat nulla pariatur. Excepteur sint occaecat cupidatat non proident,</p>
</section>

<section class="abs services">
  <h2 class="section-title">Our <em>Services</em></h2>
  <ul class="service-list">
    <li>Falcon Cloud Backup</li>
    <li>Reselling and supporting<br>Korvel Antivirus</li>
    <li>Tresby Apps</li>
  </ul>
</section>

<section class="abs who">
  <h2 class="section-title">Who <em>We Are</em></h2>
  <p class="body-text">Lorem ipsum dolor sit amet, consectetur adipisicing elit, sed do eiusmod tempor incididunt ut labore et dolore magna aliqua. Ut enim ad minim veniam, quis nostrud exercitation ullamco laboris nisi ut aliquip ex ea commodo consequat.</p>
</section>

<form class="abs coffee">
  <div class="coffee-title"><strong>Let's Meet</strong> For Coffee!</div>
  <div class="field">Name</div>
  <div class="field">Email</div>
  <div class="field-row"><div class="field">Company</div><div class="field">Phone</div></div>
  <div class="field field-area">Query Details</div>
  <div class="submit">SUBMIT</div>
</form>

<section class="abs support">
  <h2 class="section-title">Need <em>Support Now?</em></h2>
  <div class="support-photo" role="img" aria-label="Photo of a support team with headsets"></div>
  <p class="body-text">Lorem ipsum dolor sit amet, consectetur adipisicing elit, sed do eiusmod tempor incididunt ut labore et dolore magna aliqua.</p>
  <span class="help-btn">Help</span>
</section>

<section class="abs testimonial">
  <div class="testimonial-head">
    <svg width="20" height="16" viewBox="0 0 20 16"><path d="M0 16V9C0 4 2 1 7 0l1 2C5 3 4 5 4 7h4v9zM11 16V9c0-5 2-8 7-9l1 2c-3 1-4 3-4 5h4v9z" fill="#555"/></svg>
    <h2 class="section-title">What <em>Our Client's Say</em></h2>
  </div>
  <p class="testimonial-quote">Sed ut perspiciatis unde omnis iste natus error sit voluptatem accusantium doloremque laudantium, totam rem aperiam, eaque ipsa quae ab illo inventore veritatis et quasi architecto beatae vitae dicta sunt explicabo. Nemo enim ipsam voluptatem quia voluptas sit aspernatur aut odit aut fugit, sed quia consequuntur magni dolores eos qui ratione voluptatem sequi nesciunt. Neque porro quisquam est, qui dolorem ipsum quia dolor sit amet, consectetur, adipisci velit.</p>
  <div class="testimonial-name">Marta Velloni</div>
</section>

<section class="abs partners">
  <div class="abs partners-pill">Supported By</div>
  <div class="partner-row" aria-label="Partner badges">
    <span class="partner" style="width:78px;height:14px"></span>
    <span class="partner" style="width:46px;height:28px"></span>
    <span class="partner" style="width:52px;height:20px;border-radius:6px"></span>
    <span class="partner" style="width:70px;height:14px"></span>
    <span class="partner" style="width:22px;height:24px;border-radius:11px"></span>
    <span class="partner" style="width:34px;height:28px"></span>
  </div>
</section>

<section class="abs band">
  <div class="abs band-text">Do you like Our work? Want to like Us?<br>Call us on 1300 62 19 40</div>
  <div class="social" aria-label="Social links">
    <span class="social-dot"></span><span class="social-dot"></span><span class="social-dot"></span>
  </div>
</section>

<footer class="abs footer">
  <div class="abs foot-col" style="left:92px">
    <div class="foot-head">SERVICES</div>
    <ul class="foot-list" style="margin-top:-4px">
      <li>Falcon Cloud Backup</li>
      <li>Reselling and supporting Korvel Antivirus</li>
      <li>Tresby Apps</li>
    </ul>
  </div>
  <div class="abs foot-col" style="left:298px">
    <div class="foot-head">VISIT</div>
    <p class="foot-text">2001 Sed ut perspiciatis<br>Omnis, WA 45781<br>Sit voluptatem</p>
  </div>
  <div class="abs foot-col" style="left:425px;width:270px">
    <div class="foot-head">FOLLOW US ON CHATTERLY</div>
    <p class="foot-text">@kestrelnet Proin non reos mauris, in suscipit nisl. Mauris http://vireo.co/sitamet sem but I must explain to you how all this mistaken idea of denouncing</p>
    <div class="foot-time">2 hours ago</div>
  </div>
  <div class="abs foot-rule"></div>
  <div class="abs foot-mark"></div>
  <ul class="abs foot-links">
    <li>HOME</li><li>PRODUCTS</li><li>ABOUT</li><li>DOWNLOADS</li><li>CONTACT US</li>
  </ul>
  <div class="abs copyright">© Falcon Tech 2012</div>
</footer>

</body>
</html>
```